Business card design for Tolvin Waste

I would like double-sided business cards for myself and my partner that includes our logo and the existing colour scheme. We provide waste and environmental services to customers in the motor-vehicle and engineering industries.

```html
<!DOCTYPE html>
<html lang="en">
<head>
<meta charset="utf-8">
<title>Tolvin Waste – Business Card</title>
<link rel="stylesheet" href="https://fonts.googleapis.com/css2?family=Orbitron:wght@800&family=Open+Sans:wght@400;600&display=swap">
<style>
  :root {
    --leaf-light: #a8cf38;
    --leaf-dark: #6aa443;
    --name-green: #7fbb3f;
    --ink: #3c3c3c;
    --ink-soft: #4d4d4d;
    --paper: #ffffff;
    --backdrop: #e4e5e6;
  }
  * { margin: 0; padding: 0; box-sizing: border-box; }
  html, body { width: 1200px; height: 1200px; overflow: hidden; }
  body { background: var(--backdrop); position: relative; font-family: "Open Sans", sans-serif; }

  .card {
    position: absolute; left: 150px; width: 900px; height: 540px;
    background: var(--paper); overflow: hidden;
  }
  .card--front { top: 34px; }
  .card--back { top: 614px; }
  .card__accent { position: absolute; inset: 0; width: 900px; height: 540px; }

  .brand { position: absolute; display: flex; align-items: center; }
  .brand__dot { border-radius: 50%; border: 6px solid var(--leaf-dark); flex: none; }
  .brand__name { font-family: "Open Sans", sans-serif; font-weight: 600; color: var(--ink); white-space: nowrap; }

  .card--front .brand { left: 117px; top: 92px; gap: 14px; }
  .card--front .brand__dot { width: 70px; height: 70px; }
  .card--front .brand__name { font-size: 40px; }

  .holder__name {
    position: absolute; left: 117px; top: 204px;
    font-family: "Orbitron", sans-serif; font-weight: 800;
    font-size: 37px; letter-spacing: 2px; color: var(--name-green);
  }
  .holder__role {
    position: absolute; left: 117px; top: 253px;
    font-size: 23px; color: var(--ink);
  }
  .contact { position: absolute; left: 120px; top: 304px; list-style: none; }
  .contact__item {
    display: flex; align-items: center; height: 36px;
    font-size: 24px; color: var(--ink);
  }
  .contact__icon { width: 20px; height: 20px; margin-right: 18px; flex: none; }

  .card--back .brand { left: 322px; top: 100px; gap: 22px; }
  .card--back .brand__dot { width: 150px; height: 150px; border-width: 10px; }
  .card--back .brand__name { font-size: 62px; }

  .tagline {
    position: absolute; left: 330px; top: 291px;
    font-size: 23px; letter-spacing: 3.6px; color: var(--ink-soft); white-space: nowrap;
  }
  .service-icons {
    position: absolute; left: 330px; top: 358px; width: 484px; height: 104px;
    border-radius: 18px;
    background: linear-gradient(180deg, #b6d94a 0%, #7cb342 100%);
  }
</style>
</head>
<body>

<section class="card card--front">
  <svg class="card__accent" viewBox="0 0 900 540" aria-hidden="true">
    <path fill="var(--leaf-light)" d="M640,0 H900 V540 H560 C700,470 780,360 780,250 C780,140 720,60 640,0 Z"/>
    <path fill="var(--leaf-dark)" d="M770,0 H820 C870,120 880,360 720,540 H650 C820,380 830,160 770,0 Z"/>
  </svg>

  <div class="brand">
    <span class="brand__dot"></span>
    <span class="brand__name">Tolvin Waste</span>
  </div>

  <h1 class="holder__name">YOUR NAME HERE</h1>
  <p class="holder__role">Owner / Director</p>

  <ul class="contact">
    <li class="contact__item">
      <svg class="contact__icon" viewBox="0 0 24 24"><path fill="var(--leaf-dark)" d="M6.6 10.8a15.1 15.1 0 0 0 6.6 6.6l2.2-2.2c.3-.3.7-.4 1-.2 1.1.4 2.3.6 3.6.6.6 0 1 .4 1 1V20c0 .6-.4 1-1 1A17 17 0 0 1 3 4c0-.6.4-1 1-1h3.5c.6 0 1 .4 1 1 0 1.3.2 2.5.6 3.6.1.3 0 .7-.2 1z"/></svg>
      555.555.0187
    </li>
    <li class="contact__item">
      <svg class="contact__icon" viewBox="0 0 24 24"><rect x="2" y="5" width="20" height="14" fill="var(--leaf-dark)"/><path d="M2 5 L12 13 L22 5" fill="none" stroke="#fff" stroke-width="1.8"/></svg>
      tolvinwaste@mail.com
    </li>
    <li class="contact__item">
      <svg class="contact__icon" viewBox="0 0 24 24" fill="none" stroke="var(--leaf-dark)" stroke-width="2"><circle cx="12" cy="12" r="10"/><ellipse cx="12" cy="12" rx="4.5" ry="10"/><path d="M2 12h20M4 7h16M4 17h16"/></svg>
      tolvinwaste.com
    </li>
    <li class="contact__item">
      <svg class="contact__icon" viewBox="0 0 24 24"><path fill="var(--leaf-dark)" d="M12 2a7 7 0 0 0-7 7c0 5.2 7 13 7 13s7-7.8 7-13a7 7 0 0 0-7-7zm0 9.5A2.5 2.5 0 1 1 12 6.5a2.5 2.5 0 0 1 0 5z"/></svg>
      Port Halden, Westmere
    </li>
  </ul>
</section>

<section class="card card--back">
  <svg class="card__accent" viewBox="0 0 900 540" aria-hidden="true">
    <path fill="var(--leaf-light)" d="M0,0 H260 C180,60 120,140 120,250 C120,360 200,470 340,540 H0 Z"/>
    <path fill="var(--leaf-dark)" d="M130,0 H80 C30,120 20,360 180,540 H250 C80,380 70,160 130,0 Z"/>
  </svg>

  <div class="brand">
    <span class="brand__dot"></span>
    <span class="brand__name">Tolvin Waste</span>
  </div>

  <p class="tagline">WASTE &amp; ENVIRONMENTAL SERVICES</p>

  <div class="service-icons" role="img" aria-label="Row of five green eco illustrations on leaves: flower, power plug, recycling arrows, waste bin and factory chimneys"></div>
</section>

</body>
</html>
```